Fundvane Informational Banners for Ashen Tide Rising

Hello, We are currently in the Process of doing a Fundvane Campaign which is due on the 4th. We need a Grungy/Dirty Dark Dead Feeling set of Banners, and Informational Pieces in Various Sizes.
Banner Sizes:
640px × 88px Normall Banner
640px × 57px Breaker Banner
700px × 93px Header Banner
640px × 635px Display Box for Rewards
A Larger box, that needs to have a Seamless beginning and ending also needs to be made, so it can be extended as more text and so-forth is completed.

We are looking for very Dead, Dark looking images, thesr are ment to be displayed on the fundvane webpage they need to flow well with the fundvane form, as well as show off our things, simple or advanced. They need to match our style.

NOTE IMPORTANT!!!!
THESE ARE NOT ADVERTISING BANNERS, THESE ARE BANNERS FOR THE FUNDVANE WEBSITE FOR A CAMPAIGN PLEASE DO SOME HOMEWORK BEFORE ATTEMPTING THESE IMAGES WE ARE NOT LOOKING FOR ADVERTISING BANNERS WE ARE LOOKING FOR INFORMATIONAL PIECES

Example of words that will be used on the various Banners

"Physical Add-ons"
"Digital Add-ons"
"Who we are"
"What is Ashen Tide Rising?"
"What is Procedural Generation?"
"Why are you Attempting this?"

THESE ARE EXAMPLE SENTENCES THAT WILL BE IN THE BANNERS I REPEAT THESE ARE NOT ADVERTISING WEBBANNERS
Updates

Everyone is Doing wonderful, thank you all for making such lovely work. thank You. Keep it up, remember undead feel, it must be functional piece on the fundvane website. :3 

Target Market(s)

Zombie, and Undead ages People 13-51 that are Gamers

Industry/Entity Type

Digital

Requirements
Must have
• These Designs must be Boxes and Banners, and Break Points for a Fundvane Information Display I will provide a few links here.
http://www.fundvane-example.com/projects/brevmoor/harrow-veils-of-quillan
http://www.fundvane-example.com/projects/corvale/venture-paragon

Our Artwork Style & Concept Artwork can be found here
http://www.gamevault-example.net/games/ashen-tide-rising/images

```html
<!DOCTYPE html>
<html lang="en">
<head>
<meta charset="utf-8">
<title>Ashen Tide Rising — Section Banner</title>
<link rel="stylesheet" href="https://fonts.googleapis.com/css2?family=Carlito&display=swap">
<style>
  :root {
    --banner-width: 1200px;
    --banner-height: 165px;
    --ink-black: #0c0504;
    --blood-deep: #2a0806;
    --blood-mid: #5e0e09;
    --blood-glow: #8a150c;
    --ember-dark: #24120a;
    --bone-warm: #6a4a2c;
    --heading-red: #ee1a1c;
  }

  html, body {
    margin: 0;
    padding: 0;
    width: var(--banner-width);
    height: var(--banner-height);
    overflow: hidden;
    background: var(--ink-black);
  }

  .section-banner {
    position: relative;
    width: var(--banner-width);
    height: var(--banner-height);
    overflow: hidden;
  }

  .section-banner__artwork {
    position: absolute;
    inset: 0;
    background:
      radial-gradient(ellipse 260px 120px at 1010px 95px, var(--bone-warm) 0%, rgba(106, 74, 44, 0) 70%),
      radial-gradient(ellipse 360px 160px at 980px 110px, var(--ember-dark) 0%, rgba(36, 18, 10, 0) 80%),
      radial-gradient(ellipse 420px 140px at 180px 40px, var(--blood-glow) 0%, rgba(138, 21, 12, 0) 75%),
      radial-gradient(ellipse 380px 130px at 560px 60px, var(--blood-mid) 0%, rgba(94, 14, 9, 0) 75%),
      radial-gradient(ellipse 300px 120px at 380px 150px, var(--blood-mid) 0%, rgba(94, 14, 9, 0) 75%),
      linear-gradient(90deg, var(--blood-deep) 0%, var(--blood-mid) 30%, var(--blood-deep) 60%, var(--ink-black) 100%);
  }

  .section-banner__vignette {
    position: absolute;
    inset: 0;
    background: radial-gradient(ellipse 80% 120% at 50% 50%, rgba(0, 0, 0, 0) 55%, rgba(0, 0, 0, 0.6) 100%);
  }

  .section-banner__title {
    position: absolute;
    left: 34px;
    top: 57px;
    margin: 0;
    font-family: "Carlito", "Calibri", sans-serif;
    font-weight: 400;
    font-size: 54px;
    line-height: 1;
    color: var(--heading-red);
    white-space: nowrap;
  }
</style>
</head>
<body>
  <header class="section-banner">
    <div class="section-banner__artwork" role="img" aria-label="Dark grungy blood-red backdrop with a skeletal undead creature coiled on the right"></div>
    <div class="section-banner__vignette"></div>
    <h2 class="section-banner__title">What is Procedural Generation?</h2>
  </header>
</body>
</html>
```